Simple website design to introduce our software product.

Hello there! If you please, we want a lot of images (attached) to have this site to have our prospects thinking about how great it will be to use this product in their facility/clinic/office. There are a lot of happy people in the images attached and this is the feeling we want to convey...with a modern technology edge since our product digitizes the patient survey process and is used on a tablet PC.

We are finalizing a name change of our product, it is currently called "QVTR" but we are considering coming up with a better name so in the interim we will use QVTR as a place holder. The website domain where this site will reside is www.thepollharbor.com

1. We would like large scrolling images SIMILAR TO the top portion of this website : http://brightlanestudio.example/
Here are the verbiage blurbs to accompany the scrolling images:
Welcome to the next generation of Patient Experience Data Collection and Reporting. Presenting QVTR.

QVTR captures patient, nurse, doctor, employee and visitor satisfaction information in real time quickly and easily on a tablet PC.

QVTR gives you instantaneous benchmarking and reporting data including comparison reports, return rates, percentile rankings, positive and negative trending and much more.

QVTR DRAMATICALLY increases survey return rates.

QVTR empowers you to improve patient care when the data is relevant: NOW.

2. Please add something like the attached form called "QVTR info for pricing form" that says, "You won't believe our pricing! Click here" that includes the required fields as in the attached example.

3. We also want to highlight our Eco Trade Accreditation so please include the verbiage (from our company website): https://www.qvtrcorp.example/green.cfm I can provide you with the script to add the seal at the bottom left of the page.

4. We will provide verbiage for the About Us page and the Contact Us page

5. We would like to embed a video into the site and I can email you that code.

6. Please add the attached PLATINUM Eco Trade Accreditation logo on all pages and link it to this: http://www.etx.example/members/showseal/QkR4Nw==/WmVwaHlyVg==/

Looking forward to seeing what you present! Thank you for your entries. : )

We are very happy after seeing your designs.  Thank you so much.  Our product will be named The Poll Harbor, please update any and all instances of "QVTR" accordingly.  

Please be creative about this - How can an image of the tablet pc be used to navigate the site or maybe a specific section of the site?  

We have the domain www.thepollharbor.com and it is currently on a Weebly platform.  Could you/your team also launch our design on Weebly/Wordpress for us?

Hello!  Please be sure that the verbiage on your page designs is NOT pulled from our company website, QVTRience (qvtrcorp.example).  This is our PRODUCT website, not our COMPANY website.

Please make the site design concise.  Please include the following elements:  

1.  All designs must have a box (similar to file number 10 that is attached to the brief)
The title of the box needs to be "You won't believe our pricing!"
and has the following required fields:

*first name
*last name
*email
*phone
*company 
The submit button should say "GET IT!"  The position of this box should be on the right side of the page and while we want site visitors to see this box, we don't want it to be the first thing that draws their eye.  In other words, place this box softly/subtly on the site.  

2.  We like the images of the tablet pc.  It is very important that the site include pictures of PATIENTS with the tablet pc in their hands.  For this software, images of patients holding the tablet are more in alignment with the image we're trying to brand than are images of doctors/nurses holding the tablet pc. 

3.  Please update all designs to have the lead header/verbiage say "Welcome to the next generation of Patient Experience Data Collection and Reporting.  Presenting The Poll Harbor."  

4.  Please add this to the design too (if it's not already in your design), "Collect patient, doctor, nurse, employee and visitor Satisfaction/Experience feedback quickly, easily and in REAL TIME on a tablet pc."   

Please include this verbiage on the website - Users of The Poll Harbor consistently enjoy a survey return rate ABOVE 90%!

Target Market(s)

Healthcare facilities/hospitals/clinics/doctor's offices (initially, but the product can be customized for any industry).

Industry/Entity Type

Software

```html
<!DOCTYPE html>
<html lang="en">
<head>
<meta charset="utf-8">
<title>QVTRience Inc. – Patient Experience in Real-Time</title>
<link href="https://fonts.googleapis.com/css2?family=Arimo:wght@400;700&family=Roboto:wght@300;400&family=Oswald:wght@400&display=swap" rel="stylesheet">
<style>
:root{
  --page-bg:#e8f1fa;
  --ink:#1f2f45;
  --navy:#2a3f5f;
  --footer:#354a66;
  --footer-dark:#243650;
  --link:#6f95bd;
  --list-bg:#e4effc;
  --hero-a:#8a9eb6;
  --hero-b:#b6c4d4;
  --ad-bg:#2d4262;
  --cta:#d8281c;
  --white:#ffffff;
  --body:#333b46;
}
*{box-sizing:border-box;margin:0;padding:0}
html,body{width:1022px;height:1200px;overflow:hidden}
body{background:var(--page-bg);font-family:"Arimo",Arial,sans-serif;color:var(--body)}
.site{position:absolute;left:127px;top:0;width:768px;height:1200px;background:var(--white);box-shadow:0 0 8px rgba(0,0,0,.15)}
.site::before{content:"";position:absolute;left:0;top:0;width:100%;height:4px;background:var(--navy)}
.utility{position:absolute;right:18px;top:4px;height:15px;padding:0 9px;background:var(--navy);color:var(--white);font-size:9px;line-height:15px;display:flex;gap:6px}
.utility .sep{font-size:7px}
.brand-mark{position:absolute;left:21px;top:11px;width:53px;height:53px;background:var(--navy)}
.brand-name{position:absolute;left:82px;top:17px;font-family:"Roboto",sans-serif;font-weight:300;font-size:24px;line-height:26px;color:var(--navy);white-space:nowrap}
.brand-tag{position:absolute;left:83px;top:46px;font-size:8.5px;line-height:10px;color:var(--link);white-space:nowrap}
.nav{position:absolute;right:18px;top:43px;display:flex;gap:19px;font-size:11px;color:var(--link)}
.nav .current{color:var(--ink)}
.hero{position:absolute;left:0;top:72px;width:768px;height:333px;background:linear-gradient(90deg,var(--hero-a),var(--hero-b))}
.hero-photo{position:absolute;right:80px;top:0;width:270px;height:333px;background:linear-gradient(180deg,#c8d2dd,#e9edf2)}
.hero-copy{position:absolute;left:68px;top:112px;color:var(--white);font-family:"Roboto",sans-serif;font-weight:300}
.hero-copy p{font-size:19px;line-height:22px}
.hero-copy .present{font-size:27px;margin-top:4px}
.hero-copy .present b{font-weight:300;font-size:40px}
.hero-arrow{position:absolute;top:133px}
.hero-arrow.prev{left:16px}.hero-arrow.next{right:16px}
.dots{position:absolute;left:360px;top:307px;display:flex;gap:3px}
.dots i{width:7px;height:7px;border-radius:50%;background:var(--navy)}
.dots i:first-child{background:var(--white)}
.intro{position:absolute;left:31px;top:448px;width:462px}
.intro h1{font-family:"Roboto",sans-serif;font-weight:400;font-size:21px;color:var(--ink);margin-bottom:12px}
.intro p{font-size:8.6px;line-height:13.2px;margin-bottom:9px}
.checklist{background:var(--list-bg);padding:10px 24px;list-style:none;font-size:8.6px;line-height:10.5px;color:var(--ink);margin:22px 0 24px;width:457px}
.checklist li{position:relative;margin:6px 0}
.checklist li::before{content:"";position:absolute;left:-10px;top:3px;width:4px;height:4px;border-radius:50%;background:var(--ink)}
.pricing{position:absolute;left:529px;top:458px;width:211px;height:297px;background:var(--ad-bg);overflow:hidden}
.pricing-title{position:absolute;right:10px;top:14px;text-align:right;font-family:"Oswald",sans-serif;color:var(--white);font-size:34px;line-height:36px;letter-spacing:-.5px}
.pricing-title span{font-size:29px}
.pricing-photo{position:absolute;left:0;top:92px;width:130px;height:205px;background:linear-gradient(180deg,#4e6485,#c9d3de)}
.pricing-cta{position:absolute;left:99px;top:133px;width:95px;height:29px;background:var(--cta);color:var(--white);font-size:13px;line-height:29px;text-align:center;box-shadow:0 1px 2px rgba(0,0,0,.4)}
.video{position:absolute;left:529px;top:787px;width:211px;height:165px;background:#000}
.video-play{position:absolute;left:97px;top:62px}
.video-bar{position:absolute;left:0;bottom:0;width:100%;height:23px;background:#1a1a1a;display:flex;align-items:center;gap:8px;padding:0 6px;color:var(--white);font-size:7px}
.video-track{width:72px;height:3px;background:#555}
.footer{position:absolute;left:0;top:997px;width:768px;height:177px;background:var(--footer);color:var(--white)}
.badge{position:absolute;left:34px;top:40px;width:149px;height:92px;background:#8dc63f;border-radius:10px}
.divider{position:absolute;top:38px;width:1px;height:96px;background:rgba(255,255,255,.15)}
.f-col{position:absolute;top:50px}
.f-col h3{font-weight:400;font-size:13px;margin-bottom:12px}
.f-col address{font-style:normal;font-size:9px;line-height:13.5px;font-weight:700}
.icons{display:flex;gap:9px}
.icons i{width:15px;height:15px;background:var(--white);border-radius:2px}
.f-brand{position:absolute;left:610px;top:48px;width:130px;text-align:center}
.f-brand .mark{width:44px;height:44px;background:var(--white);margin:0 auto 12px}
.f-brand .name{font-family:"Roboto",sans-serif;font-weight:300;font-size:17px}
.legal{position:absolute;left:0;top:1174px;width:768px;height:26px;background:var(--footer-dark);color:#a9b6c7;font-size:8px;line-height:26px;text-align:center}
</style>
</head>
<body>
<div class="site">
  <header>
    <div class="utility"><span>Blog</span><span class="sep">•</span><span>Login</span></div>
    <div class="brand-mark"></div>
    <div class="brand-name">QVTRience Inc.</div>
    <div class="brand-tag">Improving the Patient Experience in Real-Time</div>
    <nav class="nav"><span class="current">Home</span><span>About Us</span><span>QVTR Features</span><span>Join The Team</span><span>Contact Us</span></nav>
  </header>

  <section class="hero">
    <div class="hero-photo" role="img" aria-label="Smiling patient holding a tablet showing a survey heart"></div>
    <div class="hero-copy">
      <p>Welcome to the next generation of Patient<br>Experience Data Collection and Reporting.</p>
      <p class="present">Presenting <b>QVTR</b></p>
    </div>
    <svg class="hero-arrow prev" width="24" height="52" viewBox="0 0 24 52"><path d="M22 2 L2 26 L22 50" fill="none" stroke="#fff" stroke-width="2"/></svg>
    <svg class="hero-arrow next" width="24" height="52" viewBox="0 0 24 52"><path d="M2 2 L22 26 L2 50" fill="none" stroke="#fff" stroke-width="2"/></svg>
    <div class="dots"><i></i><i></i><i></i><i></i><i></i></div>
  </section>

  <main class="intro">
    <h1>Welcome to The Poll Harbor</h1>
    <p>Collect patient, doctor, nurse, employee and visitor Satisfaction/Experience feedback quickly, easily and in REAL TIME on a tablet pc. The Poll Harbor gives you instantaneous benchmarking and reporting data including comparison reports, return rates, percentile rankings, positive and negative trending and much more. Users of The Poll Harbor consistently enjoy a survey return rate ABOVE 90%!</p>
    <p>Healthcare facilities, hospitals, clinics and doctor's offices have told us that change is needed in how survey data is collected; many are frustrated with their patient satisfaction scores and reports when:</p>
    <ul class="checklist">
      <li>Return rates were not correct or entirely too low</li>
      <li>Surveys were lost in the mail or not processed yet as the vendor did not receive the mail delivery containing that month's batch of surveys</li>
      <li>Benchmark reports were late (45 days after the close of each quarter)</li>
      <li>The data was incorrect due to a misread survey scan and surveys that were not legible or improperly filled out</li>
    </ul>
    <p>The Poll Harbor empowers you to improve patient care when the data is relevant: NOW. Placing a tablet pc in the hands of your patients turns every visit into a chance to listen, and real-time data collection becomes the new "norm". Imagine what your facility could do:</p>
    <ul class="checklist">
      <li>What if you could use a modern tablet to collect patient satisfaction data at the point of care?</li>
      <li>What if comparison and benchmark reports could be made available in real-time?</li>
      <li>What if you could translate the survey to the language that is most convenient to the patient on the fly?</li>
      <li>What if you could increase your return rate to record highs by demonstrating real compassion and concern when asking for their valuable perception of the care they received?</li>
      <li>What if your patient satisfaction/experience data could offer you a real opportunity to improve patient care immediately?</li>
      <li>And what if you could add/edit/create your own questions/surveys that were relevant to your practice?</li>
    </ul>
  </main>

  <aside class="pricing">
    <div class="pricing-photo" role="img" aria-label="Smiling doctor with stethoscope, arms crossed"></div>
    <div class="pricing-title">You won't believe<br><span>our pricing!</span></div>
    <div class="pricing-cta">Click here</div>
  </aside>

  <div class="video">
    <svg class="video-play" width="14" height="16" viewBox="0 0 14 16"><path d="M0 0 L14 8 L0 16Z" fill="#fff"/></svg>
    <div class="video-bar">
      <svg width="7" height="8" viewBox="0 0 7 8"><path d="M0 0 L7 4 L0 8Z" fill="#fff"/></svg>
      <span>00:00</span><div class="video-track"></div>
    </div>
  </div>

  <footer class="footer">
    <div class="badge" role="img" aria-label="Platinum eco trade accreditation seal"></div>
    <div class="divider" style="left:209px"></div>
    <div class="f-col" style="left:237px">
      <h3>CONTACT</h3>
      <address>QVTRience<br>Mobile Office 1<br>Fairhaven Northstate<br>555-014-QVTR (7887)</address>
    </div>
    <div class="divider" style="left:370px"></div>
    <div class="f-col" style="left:394px">
      <h3>Connect With Us</h3>
      <div class="icons"><i></i><i></i><i></i></div>
    </div>
    <div class="divider" style="left:517px"></div>
    <div class="f-col" style="left:540px">
      <h3>Blog</h3>
      <div class="icons"><i></i></div>
    </div>
    <div class="divider" style="left:589px"></div>
    <div class="f-brand"><div class="mark"></div><div class="name">QVTRience Inc.</div></div>
  </footer>
  <div class="legal">© QVTRience Inc 2014. All Rights Reserved</div>
</div>
</body>
</html>
```